bramblegate crest roofing flyer*

I need an a5 size flyer designing to go in our local advertising magazine.We are based in the north west of England Id like key features from the website including on the flyer, possibly even reviews, what we do ect.I don't however want it too busy, simple pictures and description of service.company colours and logo. I require simple one sided business cards toonumber, web address and logowinner will receive a request to design around 5 different double sided a5 flyers too, each with all our services on one side and the other primarily for one service we have provided locally with a spacve to put the house number down.REPAIRSROOFLINEFLAT ROOFS PITCHED ROOFSSYNTHETIC ROOFSUP TO 50 YEARS WARRANTY AVAILABLERANKED THE #1 FLAT ROOFER IN THE UK OUT OF 787 REGISTERED FLAT ROOFING COMPANIESRANKED THE #10 ROOFING COMPANY IN THE UK OUT OF 1976 REGISTERED SPECIALIST ROOFING COMPANIESBOTH FOR COST, CUSTOMER SERVICE AND QUALITY WITH 5 STAR REVIEWSGUARANTEED TO FIND AND FIX A LEAKAPPROVED INSTALLERSAWARD WINNINGTIME SERVED FIXED PRICES

Target Market(s)

homeowners

Colors

Designer to choose only greyscale colors for use in the design.

Requirements
Must have
• contact details
• pictures of my work
• clear and simple

```html
<!DOCTYPE html>
<html lang="en">
<head>
<meta charset="utf-8">
<title>Bramblegate Crest Roofing — A5 Flyer</title>
<link href="https://fonts.googleapis.com/css2?family=Oswald:wght@500;600&family=Source+Sans+3:wght@400;600;700&display=swap" rel="stylesheet">
<style>
  :root {
    --green: #4a9a3c;
    --green-dark: #3f8a33;
    --yellow: #f5c400;
    --charcoal: #262626;
    --shingle: #303030;
    --ink: #1a1a1a;
    --white: #ffffff;
    --backdrop: #d4d4d4;
  }
  * { margin: 0; padding: 0; box-sizing: border-box; }
  html, body {
    width: 1200px; height: 1200px; overflow: hidden;
    background: var(--backdrop);
  }
  .flyer {
    position: absolute; left: 211px; top: 49px;
    width: 778px; height: 1102px;
    background: var(--white);
    overflow: hidden;
  }
  .hero { position: absolute; left: 0; top: 0; width: 778px; height: 616px; display: block; }
  .headline { font-family: "Oswald", sans-serif; font-weight: 600; fill: var(--white); }
  .headline--small { fill: var(--ink); }
  .brand-name { font-family: "Oswald", sans-serif; font-weight: 600; fill: var(--green); }
  .service-label {
    font-family: "Source Sans 3", sans-serif; font-weight: 600;
    font-size: 16px; fill: var(--white); text-anchor: middle;
  }
  .gallery { position: absolute; left: 0; top: 634px; width: 778px; height: 160px; display: block; }
  .about {
    position: absolute; left: 0; top: 813px; width: 778px; height: 144px;
    background: var(--green);
    border-bottom: 6px solid var(--yellow);
    padding: 14px 14px 0 16px;
    font-family: "Source Sans 3", sans-serif; font-size: 21px; line-height: 27px;
    color: var(--white); text-align: justify; letter-spacing: -0.1px;
  }
  .contact {
    position: absolute; left: 0; top: 963px; width: 778px; height: 139px;
    background: linear-gradient(#ffffff, #eeeeee);
    text-align: center; font-family: "Source Sans 3", sans-serif;
  }
  .contact__lines { padding-top: 10px; font-size: 22px; font-weight: 600; line-height: 29px; color: var(--ink); }
  .contact__web { margin-top: 4px; font-size: 40px; font-weight: 700; color: var(--green); letter-spacing: 0.3px; }
</style>
</head>
<body>
<main class="flyer">
  <svg class="hero" viewBox="0 0 778 616" xmlns="http://www.w3.org/2000/svg">
    <defs>
      <linearGradient id="shingleTone" x1="0" y1="0" x2="0" y2="1">
        <stop offset="0" stop-color="#2a2a2a"/><stop offset="1" stop-color="#3a3a3a"/>
      </linearGradient>
      <linearGradient id="workPhoto" x1="0" y1="0" x2="1" y2="1">
        <stop offset="0" stop-color="#8a9a7a"/><stop offset="0.45" stop-color="#c98f4e"/><stop offset="1" stop-color="#3b3b3b"/>
      </linearGradient>
    </defs>
    <rect class="hero__roof" width="778" height="260" fill="url(#shingleTone)" role="img" aria-label="Dark roof shingle texture"/>
    <rect x="330" y="258" width="448" height="332" fill="url(#workPhoto)" role="img" aria-label="Photo of roofers laying membrane on a new pitched roof"/>
    <rect x="358" y="252" width="420" height="7" fill="var(--yellow)"/>
    <polygon points="0,142 126,78 358,250 418,258 330,482 0,482" fill="var(--green)"/>
    <polygon points="0,50 42,50 42,72 126,22 302,114 302,138 126,66 0,132" fill="var(--yellow)"/>
    <polygon points="0,482 338,482 438,590 778,590 778,616 0,616" fill="var(--charcoal)"/>

    <text class="brand-name" x="758" y="150" font-size="40" text-anchor="end" textLength="330" lengthAdjust="spacingAndGlyphs">BRAMBLEGATE CREST</text>
    <text class="brand-name" x="758" y="196" font-size="40" text-anchor="end">ROOFING</text>

    <text class="headline headline--small" x="16" y="246" font-size="62" textLength="116" lengthAdjust="spacingAndGlyphs">UP TO</text>
    <text class="headline" x="14" y="326" font-size="98" textLength="322" lengthAdjust="spacingAndGlyphs">50 YEARS</text>
    <text class="headline" x="14" y="413" font-size="88" textLength="298" lengthAdjust="spacingAndGlyphs">WARRANTY</text>
    <text class="headline" x="15" y="456" font-size="32" textLength="152" lengthAdjust="spacingAndGlyphs">RANKED THE #1</text>

    <g class="services">
      <g transform="translate(54 525)"><circle r="25" fill="var(--yellow)"/><path d="M-12,0 L-3,10 L14,-12" fill="none" stroke="var(--white)" stroke-width="6" stroke-linecap="round" stroke-linejoin="round"/></g>
      <g transform="translate(152 525)"><circle r="25" fill="var(--yellow)"/><path d="M-12,0 L-3,10 L14,-12" fill="none" stroke="var(--white)" stroke-width="6" stroke-linecap="round" stroke-linejoin="round"/></g>
      <g transform="translate(246 525)"><circle r="25" fill="var(--yellow)"/><path d="M-12,0 L-3,10 L14,-12" fill="none" stroke="var(--white)" stroke-width="6" stroke-linecap="round" stroke-linejoin="round"/></g>
      <g transform="translate(344 525)"><circle r="25" fill="var(--yellow)"/><path d="M-12,0 L-3,10 L14,-12" fill="none" stroke="var(--white)" stroke-width="6" stroke-linecap="round" stroke-linejoin="round"/></g>
      <text class="service-label" x="54" y="574">REPAIRS</text><text class="service-label" x="54" y="595">ROOFLINE</text>
      <text class="service-label" x="152" y="574">FLAT</text><text class="service-label" x="152" y="595">ROOFS</text>
      <text class="service-label" x="246" y="574">PITCHED</text><text class="service-label" x="246" y="595">ROOFS</text>
      <text class="service-label" x="356" y="574">SYNTHETIC</text><text class="service-label" x="356" y="595">ROOFS</text>
    </g>
  </svg>

  <svg class="gallery" viewBox="0 0 778 160" xmlns="http://www.w3.org/2000/svg">
    <defs>
      <linearGradient id="tileWork" x1="0" y1="0" x2="1" y2="1"><stop offset="0" stop-color="#c9643a"/><stop offset="1" stop-color="#b9a488"/></linearGradient>
      <linearGradient id="gableHouse" x1="0" y1="0" x2="0" y2="1"><stop offset="0" stop-color="#8cc0e8"/><stop offset="0.55" stop-color="#4a4440"/><stop offset="1" stop-color="#b07a4c"/></linearGradient>
      <linearGradient id="brownRoof" x1="0" y1="0" x2="1" y2="1"><stop offset="0" stop-color="#6b3a2e"/><stop offset="1" stop-color="#8a4a34"/></linearGradient>
    </defs>
    <path d="M0,0 H222 Q242,0 236,18 L192,142 Q186,160 168,160 H0 Z" fill="url(#tileWork)" role="img" aria-label="Photo of a roofer fitting battens and clay tiles"/>
    <path d="M268,0 H530 Q552,0 546,20 L505,142 Q499,160 480,160 H226 L258,14 Q262,0 268,0 Z" fill="url(#gableHouse)" role="img" aria-label="Photo of a gabled house with a dark tiled roof and glazed front"/>
    <path d="M598,0 H778 V160 H545 L585,14 Q589,0 598,0 Z" fill="url(#brownRoof)" role="img" aria-label="Photo of a brown metal tile roof with a skylight"/>
  </svg>

  <section class="about">
    Flat roofer in the uk out of 787 registered flat roofing companies ranked the #10. Roofing company in the uk out of 1976 registered specialist roofing companies both for cost, customer service and quality with 5 star reviews. Guaranteed to find and fix a leak approved installers award winning time served fixed prices.
  </section>

  <footer class="contact">
    <p class="contact__lines">For More Information Contact us on 258-555-0190 or<br>Email us at info@bramblegatecrest.co.uk</p>
    <p class="contact__web">www.bramblegatecrest.co.uk</p>
  </footer>
</main>
</body>
</html>
```